Tarno Booking website (www.tarnobooking.example)

My company develops booking software, Tarno Booking, for the hourly booking of resources such as classes in a school or customer booking involving rooms in a spa. These bookings also involve the customers, staff, rooms and a lesson or treatment.

The main difference between this software and general calendar software such as Zindle calendar is that this Tarno Booking allows resources such as people and rooms to be associated with the bookings. This is important for example in the case of a Spa to make sure the rooms are booked appropriately and to see the free times for the rooms. For a golf practice range the players much be booked to the tee spots where they practice golf.

I have tried to design the website myself, as a computer programmer- I am a bit "square" and not a designer, my first attempt is http://www.tarnobooking.example/, my second attempt is at http://www.pelumwerks.example/tarnobookingwebsite/
I am not happy with my designs as compared to the professional designs I see people can come up with here. The software must have the image of a professional software product in order to inspire the confidence of customers.

Am looking for a design which will be the most likely to give the customer the following feeling:
* Confident the product can do the job.
* Feel easy to want to try it, at least for the free trial.
* Its a professional software product and also a web based product, the user can login from the web.

Look at other booking software websites for ideas, here is a list of links to similar booking products. These products all have different features but are mostly for resource booking.
http://pelumwerks.example/tarnobookingwebsite/?page=compare
Updates

Hello all,

Thankyou for the designs so far, to save peoples time, I will try to eliminate the bottom 50% of designs now.

To be honest, most of the designs are of a good or high quality, I think its very tough on you as graphic and web designers. Only a minor few are of low quality.

If your design is discarded - I would say its unlikely that you are going to be able to produce a design that will beat the competition. 
You probably already know, you could try to re-sell your design later for other projects or as a template on one of those template websites. Some of these discarded designs are quite worthwhile designs.

Best regards, Gareth

Target Market(s)

Spa, Gym, School, Golf, any organization who manages bookings of their customers

Industry/Entity Type

Software

Requirements
Must have
• Home page and inner page, any other pages up to you.

Make a logo or use the image of the girl that I already have on the second design.

Menu(s) for navigation.

A language switcher for 3 languages, English, Chinese Traditional and Chinese Simplified. (Western, Hong Kong and Chinese mainland market are important).

Space for a video introduction, it could be small and when the user clicks on it then it gets bigger then it won't take up too much space. Up to you.

A space for the user to login and register a new account.

Screenshots.

I don't have any strong preferences, use your own ideas, if you look at all the other products you can get the basic idea from them.

The total goal is to make a website which is going to lead to sales of the software product.

```html
<!DOCTYPE html>
<html lang="en">
<head>
<meta charset="utf-8">
<title>Tarno Booking – Home</title>
<link href="https://fonts.googleapis.com/css2?family=Arimo:wght@400;700&family=Roboto+Condensed:wght@400;700&display=swap" rel="stylesheet">
<style>
:root{
  --page:#ebebeb;
  --ink:#222;
  --topbar:#1f2126;
  --red:#a11d14;
  --red-dark:#6f120c;
  --orange:#f7a21d;
  --orange-dark:#e07b07;
  --panel-head:#d3d3d3;
  --login:#7f93ad;
  --login-dark:#5f7390;
  --footer:#1e1e1e;
  --footer-line:#333;
  --footer-text:#e6e6e6;
  --copyright:#8e1c14;
  --green:#6aa51e;
  --social:#3b67b0;
}
*{box-sizing:border-box;margin:0;padding:0}
html,body{width:1140px;height:1200px;overflow:hidden}
body{background:var(--page);font-family:Arimo,Arial,sans-serif;color:var(--ink);position:relative}
.abs{position:absolute}
a{color:inherit;text-decoration:none}

.top-bar{left:0;top:0;width:1140px;height:29px;background:linear-gradient(#3a3d44,var(--topbar))}
.top-links{left:396px;top:9px;font-size:10.5px;font-weight:700;color:#fff;white-space:nowrap}
.top-links .current{color:var(--orange)}
.top-links span.sep{color:#aaa;margin:0 2px}
.lang-select{left:795px;top:5px;width:157px;height:22px;background:#fff;border:1px solid #999;border-radius:2px;font-size:11px;padding:4px 0 0 26px;white-space:nowrap}
.lang-select .caret{position:absolute;right:0;top:0;width:20px;height:20px;background:#ddd;border-left:1px solid #aaa}
.lang-menu{left:795px;top:29px;width:132px;background:#f4f4f4;border:1px solid #bbb;font-size:11px;z-index:3}
.lang-menu li{list-style:none;padding:3px 0 0 24px;height:19px;white-space:nowrap}
.lang-menu li.active{color:var(--red);background:#e6e0dc}

.mascot{left:193px;top:47px;width:60px;height:84px;border-radius:8px;background:linear-gradient(#f2c453,#c9323a)}
.brand-name{left:262px;top:74px;font-size:26px;font-weight:700;color:var(--red);line-height:1.05;width:120px}

.cart{left:771px;top:72px;width:181px;height:35px;background:#4a4a4a;border-radius:4px;color:#ddd;font-size:11px;padding:12px 0 0 50px}
.cart .checkout{position:absolute;right:4px;top:5px;width:74px;height:25px;background:var(--green);border-radius:3px;color:#fff;font-weight:700;font-size:11px;text-align:center;line-height:25px}

.main-nav{top:115px;height:24px;font-size:12px;font-weight:700;text-align:center;line-height:22px;white-space:nowrap;background:linear-gradient(#ffc04a,var(--orange-dark));border:1px solid #c46a06;color:#3a1d00}
.main-nav.current{background:linear-gradient(#c9352a,var(--red-dark));color:#fff;border-color:#5a0c08}

.hero{left:185px;top:146px;width:768px;height:272px;background:#fff;border-radius:6px;box-shadow:0 14px 16px -10px rgba(0,0,0,.35)}
.hero-inner{left:3px;top:3px;width:762px;height:266px;border-radius:5px;background:radial-gradient(ellipse at 35% 45%,#c2261b,var(--red-dark) 85%);overflow:hidden}
.hero-photo{right:0;top:0;width:245px;height:266px;background:linear-gradient(100deg,rgba(0,0,0,0),#3c3f4c 40%,#2a2d38)}
.quote-mark{font-family:Georgia,serif;font-size:62px;color:#fff;font-weight:700;line-height:1}
.hero-quote{left:76px;top:50px;width:460px;font-family:'Roboto Condensed',sans-serif;font-weight:700;font-size:21px;line-height:28px;color:#fff}
.hero-cite{left:76px;top:136px;font-size:13px;color:#1b0000;line-height:17px}
.hero-rule{left:40px;top:190px;width:460px;height:2px;background:linear-gradient(90deg,transparent,#e2493e,transparent)}
.hero-cta{left:76px;top:222px;color:#fff;font-size:13.5px;white-space:nowrap}
.learn-more{left:290px;top:210px;width:120px;height:32px;border-radius:16px;background:linear-gradient(#fff,#bdbdbd);color:#333;font-size:13px;font-weight:700;font-style:italic;text-align:center;line-height:32px}
.hero-arrow{top:260px;width:24px;height:32px;background:#1b1b1b;z-index:2}

.panel{top:455px;height:172px;background:#fff;border:1px solid #cfcfcf;border-radius:3px;box-shadow:0 10px 12px -8px rgba(0,0,0,.3)}
.panel-head{height:34px;background:linear-gradient(#efefef,var(--panel-head));font-size:12.5px;font-weight:700;text-align:center;line-height:34px;color:#333;border-bottom:1px solid #bbb;white-space:nowrap}
.panel-body{padding:8px 11px;font-size:10.5px;line-height:13px;color:#222}
.panel-body.justify{text-align:justify}
.panel-body .highlight{color:var(--red);font-style:italic;font-weight:700;text-decoration:underline}
.panel-body .tight{letter-spacing:-0.2px;white-space:nowrap}
.read-more{width:86px;height:24px;border-radius:12px;background:linear-gradient(#fff,#c6c6c6);border:1px solid #aaa;font-size:11px;font-weight:700;font-style:italic;text-align:center;line-height:22px;color:#333}
.login{left:707px;top:455px;width:245px;height:172px;background:linear-gradient(#93a5bd,var(--login-dark));border:1px solid #566a85;border-radius:3px}
.login .panel-head{font-size:14px;font-weight:400}
.field-label{font-size:12px;color:#111}
.field{background:#fff;border:1px solid #8796aa;border-radius:4px;height:22px;font-size:10px;color:#888;padding:4px 0 0 18px}
.download{left:16px;top:101px;width:211px;height:50px;border-radius:25px;background:linear-gradient(#ffbe2a,#ed7a03);border:1px solid #b85a00;text-align:center;color:#3a1700}
.download b{display:block;font-size:22px;line-height:24px;margin-top:3px}
.download span{font-size:13px}
.terms{left:0;top:157px;width:243px;text-align:center;font-size:10px;font-style:italic;text-decoration:underline;color:#222}

.divider{left:253px;top:665px;width:634px;border-top:1px dashed #bbb}

.ribbon{top:697px;height:32px;width:135px;background:linear-gradient(#f9b23c,var(--orange-dark));clip-path:polygon(0 0,88% 0,100% 50%,88% 100%,0 100%);color:#fff;font-size:12px;font-weight:700;line-height:32px;padding-left:9px;white-space:nowrap;box-shadow:0 4px 4px rgba(0,0,0,.2)}
.col-text{font-size:11px;line-height:14px;text-align:justify;color:#222}
.news-date{font-size:11px;font-weight:700;font-style:italic;color:var(--red)}
.news-sep{left:447px;top:823px;width:230px;border-top:1px dashed #bbb}

.video{left:709px;top:748px;width:242px;height:171px;background:#1b1b1b;box-shadow:0 6px 8px rgba(0,0,0,.3)}

.footer{left:0;top:984px;width:1140px;height:180px;background:var(--footer)}
.footer h3{position:absolute;top:40px;font-size:14.5px;font-weight:400;color:#fff}
.footer ul{position:absolute;top:72px;list-style:none;width:220px}
.footer li{font-size:11px;color:var(--footer-text);height:24px;border-bottom:1px solid var(--footer-line);padding-top:6px}
.newsletter{left:701px;top:80px;width:251px;height:27px;background:#444;font-size:11px;color:#ddd;padding:7px 0 0 16px}
.newsletter .subscribe{position:absolute;right:3px;top:3px;width:70px;height:21px;background:linear-gradient(#fff,#ccc);color:#222;font-weight:700;font-style:italic;text-align:center;line-height:21px}
.join{left:701px;top:137px;font-size:14px;color:#fff}
.social{top:127px;width:25px;height:25px;border-radius:3px;background:linear-gradient(#5d8bd6,var(--social))}
.copyright{left:0;top:1164px;width:1140px;height:36px;background:var(--copyright);color:#fff;font-size:11.5px;font-weight:700;text-align:center;line-height:36px}
</style>
</head>
<body>

<header>
  <div class="abs top-bar"></div>
  <nav class="abs top-links">
    <a class="current">Home</a><span class="sep">|</span><a>About Us</a><span class="sep">|</span><a>Why Tarno Booking</a><span class="sep">|</span><a>Downloads</a><span class="sep">|</span><a>Contact Us</a><span class="sep">|</span><a>Enquire Tarno</a>
  </nav>
  <div class="abs lang-select">Choose Language
    <span class="caret"><svg width="20" height="20"><path d="M6 8h8l-4 5z" fill="#333"/></svg></span>
  </div>
  <ul class="abs lang-menu">
    <li class="active">English</li>
    <li>Chinese</li>
    <li>Traditional Chinese</li>
  </ul>

  <div class="abs mascot" role="img" aria-label="Illustrated booking assistant mascot"></div>
  <div class="abs brand-name">Tarno<br>Booking</div>

  <div class="abs cart">$120.00<span class="checkout">Checkout</span></div>

  <nav>
    <a class="abs main-nav current" style="left:453px;width:76px">Home</a>
    <a class="abs main-nav" style="left:532px;width:132px">About Tarno Booking</a>
    <a class="abs main-nav" style="left:668px;width:69px">Videos</a>
    <a class="abs main-nav" style="left:741px;width:71px">Purchase</a>
    <a class="abs main-nav" style="left:816px;width:69px">Free Trial</a>
    <a class="abs main-nav" style="left:889px;width:63px">Compare</a>
  </nav>
</header>

<section class="abs hero">
  <div class="abs hero-inner">
    <div class="abs hero-photo" role="img" aria-label="Photo of a smiling businessman in a suit giving a thumbs up"></div>
    <div class="abs quote-mark" style="left:40px;top:30px">&ldquo;</div>
    <p class="abs hero-quote">Tarno Booking is really effective and help my firm to increase productivity.<br>Intrested in future version too. <span class="quote-mark" style="font-size:44px;vertical-align:-14px">&rdquo;</span></p>
    <p class="abs hero-cite">Maren Holt<br>Chairman, Qorvel Corp.</p>
    <div class="abs hero-rule"></div>
    <p class="abs hero-cta">See How Tarno Booking Helps you</p>
    <a class="abs learn-more">Learn more</a>
  </div>
</section>
<div class="abs hero-arrow" style="left:189px"><svg width="24" height="32"><path d="M15 9l-7 7 7 7" stroke="#fff" stroke-width="3" fill="none"/></svg></div>
<div class="abs hero-arrow" style="left:925px"><svg width="24" height="32"><path d="M9 9l7 7-7 7" stroke="#fff" stroke-width="3" fill="none"/></svg></div>

<section class="abs panel" style="left:185px;width:246px">
  <h2 class="panel-head">Benefits of Tarno Booking &rsaquo;</h2>
  <p class="panel-body justify">Tarno Booking stores all data on our servers in the SaaS model giving a very low total cost of ownership our customers. You have zero investment in server platform hardware, zero investment in software licenses, zero investment in hardware and software upgrades, as these are included as part of the service.</p>
  <a class="abs read-more" style="left:152px;top:142px">Read more</a>
</section>

<section class="abs panel" style="left:445px;width:246px">
  <h2 class="panel-head">Salient Features &rsaquo;</h2>
  <p class="panel-body">Cloud Hosted, no installation required.<br><span class="tight">Client software for Lumen®, Orchard® and Penguix</span><br><span class="highlight">Increased productivity</span><br>Add, delete change rooms bookings<br>Double-booking prevention<br>Multiple staff members<br>Robust SQL database</p>
  <a class="abs read-more" style="left:151px;top:142px">Read more</a>
</section>

<section class="abs login">
  <h2 class="panel-head">Login &amp; Get a Full working Trial</h2>
  <span class="abs field-label" style="left:11px;top:51px">User ID</span>
  <div class="abs field" style="left:69px;top:45px;width:160px">Your Email Adress</div>
  <span class="abs field-label" style="left:11px;top:74px">Password</span>
  <div class="abs field" style="left:69px;top:70px;width:160px"></div>
  <a class="abs download"><b>DOWNLOAD</b><span>Obtain your 3 months trial</span></a>
  <a class="abs terms">Terms and conditions</a>
</section>

<div class="abs divider"></div>

<section>
  <h2 class="abs ribbon" style="left:187px;width:150px">About Tarno Booking</h2>
  <div class="abs col-text" style="left:185px;top:750px;width:230px">
    <p>Tarno Booking is front office booking software which makes managing bookings, room and staff availability fast and simple. We focus on producing quality software which is powerful yet easy to use.</p>
    <p style="margin-top:14px">This is suitable for many types of business, click here to view all the available business types and to learn more about how this software can help you directly.</p>
  </div>
  <a class="abs read-more" style="left:325px;top:930px">Read more</a>
</section>

<section>
  <h2 class="abs ribbon" style="left:448px">News &amp; Updates</h2>
  <svg class="abs" style="left:447px;top:752px" width="8" height="10"><path d="M1 1l5 4-5 4" fill="none" stroke="#333" stroke-width="2"/></svg>
  <p class="abs news-date" style="left:463px;top:750px">10-Oct-2011</p>
  <p class="abs col-text" style="left:447px;top:767px;width:232px">Tarno Booking is front office booking software which makes managing bookings, room and staff availability fast and simple.</p>
  <div class="abs news-sep"></div>
  <svg class="abs" style="left:447px;top:841px" width="8" height="10"><path d="M1 1l5 4-5 4" fill="none" stroke="#333" stroke-width="2"/></svg>
  <p class="abs news-date" style="left:463px;top:839px">09-Oct-2011</p>
  <p class="abs col-text" style="left:447px;top:856px;width:232px">Tarno Booking is front office booking software which makes managing bookings, room and staff availability fast and simple.</p>
  <a class="abs read-more" style="left:600px;top:930px">Read more</a>
</section>

<section>
  <h2 class="abs ribbon" style="left:708px">Watch Video</h2>
  <div class="abs video">
    <svg width="242" height="171" font-family="Arimo,Arial,sans-serif" font-size="9">
      <rect x="11" y="12" width="220" height="140" fill="#fff"/>
      <rect x="11" y="12" width="67" height="14" fill="#f39a12"/>
      <rect x="78" y="12" width="153" height="14" fill="#a9c8f0"/>
      <rect x="11" y="26" width="220" height="14" fill="#eaeaea"/>
      <text x="36" y="36" fill="#333">Time</text>
      <text x="107" y="36" fill="#333">Room 1</text>
      <text x="190" y="36" fill="#333">Room 2</text>
      <g stroke="#bbb">
        <line x1="78" y1="26" x2="78" y2="152"/><line x1="157" y1="26" x2="157" y2="152"/>
        <line x1="11" y1="54" x2="231" y2="54"/><line x1="11" y1="68" x2="231" y2="68"/>
        <line x1="11" y1="82" x2="231" y2="82"/><line x1="11" y1="96" x2="231" y2="96"/>
        <line x1="11" y1="110" x2="231" y2="110"/><line x1="11" y1="124" x2="231" y2="124"/>
        <line x1="11" y1="138" x2="231" y2="138"/>
      </g>
      <rect x="66" y="40" width="8" height="112" fill="#ddd" stroke="#999"/>
      <g fill="#333">
        <text x="15" y="51">7:00 am</text><text x="15" y="65">7:15 am</text><text x="15" y="79">7:30 am</text>
        <text x="15" y="93">7:45 am</text><text x="15" y="107">8:00 am</text><text x="15" y="121">8:15 am</text>
        <text x="15" y="135">8:30 am</text>
      </g>
      <rect x="158" y="99" width="72" height="30" fill="#fff" stroke="#999"/>
      <text x="162" y="110" fill="#333">Ted</text>
      <rect x="0" y="156" width="242" height="15" fill="#2a2a2a"/>
      <path d="M7 160l5 3.5-5 3.5z" fill="#ccc"/>
      <rect x="20" y="162" width="120" height="3" fill="#555"/>
      <rect x="20" y="162" width="60" height="3" fill="#e23b3b"/>
      <circle cx="80" cy="163.5" r="3" fill="#ddd"/>
      <text x="146" y="166" fill="#aaa" font-size="6">0:47 / 3:16</text>
      <path d="M180 161h3l3-3v11l-3-3h-3z" fill="#ccc"/>
      <rect x="190" y="162" width="24" height="3" fill="#ccc"/>
      <rect x="222" y="159" width="10" height="8" fill="none" stroke="#ccc"/>
    </svg>
  </div>
</section>

<footer class="abs footer">
  <h3 style="left:208px">About Tarno</h3>
  <ul style="left:208px">
    <li>Frequently Asked Questions</li>
    <li>Why Choose Tarno Booking</li>
    <li>Terms of use</li>
    <li style="border:none">Contacts</li>
  </ul>
  <h3 style="left:456px">Contact Tarno</h3>
  <ul style="left:456px">
    <li>www.tarnobooking.example</li>
    <li>address here</li>
    <li>Tel.: &nbsp;555-014-2277</li>
    <li style="border:none">support@tarnobooking.example</li>
  </ul>
  <h3 style="left:701px">Tarno Newsletter Signup</h3>
  <div class="abs newsletter">Enter your email here<span class="subscribe">Subscribe</span></div>
  <p class="abs join">Join Tarno</p>
  <span class="abs social" style="left:868px"></span>
  <span class="abs social" style="left:897px"></span>
  <span class="abs social" style="left:926px"></span>
</footer>
<div class="abs copyright">Copyright © © 2011 Tarno Booking. All rights reserved</div>

</body>
</html>
```